Wedding invitation

We need a wedding invitation designed with a logo using our initials and name underneath.
We are getting married at THE VERDELLE hotel in Gstaad and we would like have our logo similar to theirs but incorporating our initials n&l (any font/case) and our names below nuriya and Laurent. The Verdelle logo can be seen on their website.
The invitation would be square with the logo on the front in stamped foil and the colour would be THE VERDELLE brown (I have the exact colour)
THE VERDELLE Brown: C45 M70 Y68 K77
THE VERDELLE Rose Gold: BRENVIK 812
Inside we would have the invitation wording and on the opposite side some contact info. There would be four inserts - accom, directions, brunch and RSVP. We will provide the wording.

```html
<!DOCTYPE html>
<html lang="en">
<head>
<meta charset="utf-8">
<title>Nuriya &amp; Laurent — Wedding Invitation</title>
<link rel="stylesheet" href="https://fonts.googleapis.com/css2?family=Federo&display=swap">
<style>
  :root {
    --backdrop: #e8e2da;
    --card-brown-light: #55291f;
    --card-brown-dark: #411a13;
    --foil-gold: #d9ab3c;
    --foil-gold-soft: rgba(217, 171, 60, 0.45);
    --ornament-tone: #8a6a3c;
  }
  * { margin: 0; padding: 0; box-sizing: border-box; }
  html, body {
    width: 1200px; height: 675px; overflow: hidden;
    background: var(--backdrop);
  }
  .canvas { position: relative; width: 1200px; height: 675px; }
  .invitation {
    position: absolute; left: 232px; top: 133px; width: 735px; height: 368px;
    background: linear-gradient(90deg, var(--card-brown-dark) 0%, var(--card-brown-light) 50%, var(--card-brown-dark) 100%);
    font-family: "Federo", sans-serif;
    color: var(--foil-gold);
  }
  .panel {
    position: absolute; top: 15px; height: 339px;
    border: 1.5px solid var(--foil-gold);
  }
  .panel--front { left: 13px; width: 338px; }
  .panel--inside { left: 381px; width: 337px; text-align: center; }

  .monogram {
    position: absolute; left: 0; width: 100%; text-align: center;
    top: 34px; font-size: 128px; line-height: 1; letter-spacing: -4px;
  }
  .ampersand-ornament {
    position: absolute; left: 88px; top: 205px; width: 148px; height: 110px;
    background: radial-gradient(ellipse at center, var(--ornament-tone) 0%, rgba(138,106,60,0.35) 60%, rgba(138,106,60,0) 100%);
    border-radius: 50%;
  }
  .couple-name { position: absolute; font-size: 33px; line-height: 1; }
  .couple-name--first { left: 30px; top: 222px; }
  .couple-name--second { left: 118px; top: 279px; }

  .line { position: absolute; left: 0; width: 100%; line-height: 1; }
  .line--greeting { top: 28px; font-size: 16px; }
  .line--occasion { top: 66px; font-size: 27px; }
  .line--date { top: 104px; font-size: 38px; }
  .line--time { top: 166px; font-size: 16.5px; }
  .line--venue { top: 196px; font-size: 34px; }
  .line--town { top: 234px; font-size: 22px; }
  .line--monogram { top: 284px; font-size: 38px; letter-spacing: -1px; }

  .corner-ornament {
    position: absolute; top: 278px; width: 66px; height: 50px;
    background: radial-gradient(ellipse at center, var(--ornament-tone) 0%, rgba(138,106,60,0) 75%);
    border-radius: 50%;
  }
  .corner-ornament--left { left: 8px; }
  .corner-ornament--right { right: 8px; }
</style>
</head>
<body>
<div class="canvas">
  <div class="invitation">
    <section class="panel panel--front">
      <div class="monogram">nl</div>
      <div class="ampersand-ornament" role="img" aria-label="Flourished ampersand ornament behind the couple's names"></div>
      <div class="couple-name couple-name--first">Nuriya</div>
      <div class="couple-name couple-name--second">Laurent</div>
    </section>
    <section class="panel panel--inside">
      <p class="line line--greeting">We would be delight to invide you</p>
      <p class="line line--occasion">TO OUR WEDDING ON</p>
      <p class="line line--date">17.08.2014</p>
      <p class="line line--time">at two o'clock in the afternoon</p>
      <p class="line line--venue">Verdelle hotel</p>
      <p class="line line--town">in Gstaad</p>
      <div class="corner-ornament corner-ornament--left" role="img" aria-label="Small flourished ampersand ornament"></div>
      <p class="line line--monogram">nl</p>
      <div class="corner-ornament corner-ornament--right" role="img" aria-label="Small flourished ampersand ornament"></div>
    </section>
  </div>
</div>
</body>
</html>
```